Buch-/eBook-Cover für psychologische Beratung
Mirell hat sehr gut verstanden worauf es mir ankam und hat das Cover sehr gut auf das bereits bestehende abgestimmt. Sie hat zuverlässig geantwortet und Korrekturwünsche präzise ausgeführt. Grosses Kompliment! Gerne wieder.
Zielgruppe
psychologische Beratung, Zielgruppe Frauen
Aufgabenstellung
Es ist ein bestehendes ebook, das ich über meine frühere Website gekauft habe. Diese wird aufgelöst. Das ebook ist nun auf brixa und soll auch auf kolvento, aber offensichtlich zieht der Titel nicht. Deshalb möchte ich den ändern.
Der neue Titel und Untertitel lautet: Atmen statt zweifeln. Leises Naschen deuten, alte Muster entwirren.
Meine Idee wäre es, als Blickfang das Wort 'Atmen' und 'Leises Naschen' hervorzuheben.
Es ist mir wichtig, dass - vielleicht mit einer Andeutung eines Tellers - sofort klar wird, dass es um Essen geht.
Das Design soll passend zum Inhalt sein (Schrift und Illustrationen).
Das eBook ist im Querformat gehalten, weil es ein Arbeitsbuch ist. Für die Werbung brauche ich aber zusätzlich eine Version, die ins Hochformat passt.
Das Design darf nicht zu überladen sein.

```html
<!DOCTYPE html>
<html lang="de">
<head>
<meta charset="utf-8">
<title>Atmen statt zweifeln – Cover</title>
<link rel="stylesheet" href="https://fonts.googleapis.com/css2?family=Jost:wght@400;600&family=Allura&display=swap">
<style>
  :root {
    --page-bg: #e6e5ea;
    --paper: #ffffff;
    --orange: #f29d3b;
    --cream: #fdeecf;
    --ink: #333333;
    --art-tone: #f6dcb4;
  }
  * { margin: 0; padding: 0; box-sizing: border-box; }
  html, body {
    width: 675px; height: 1200px; overflow: hidden;
    background: var(--page-bg);
    font-family: "Jost", sans-serif;
    color: var(--ink);
  }
  .cover {
    position: absolute;
    background: var(--paper);
    overflow: hidden;
  }
  .cover-landscape { left: 86px; top: 122px; width: 505px; height: 356px; }
  .cover-portrait { left: 160px; top: 586px; width: 355px; height: 503px; }
  .cover-shapes { position: absolute; inset: 0; width: 100%; height: 100%; }
  .shape-cream { fill: var(--cream); }
  .shape-orange { fill: var(--orange); }
  .author { position: absolute; font-size: 11.5px; letter-spacing: 0.3px; white-space: nowrap; }
  .title-script {
    position: absolute; font-family: "Allura", cursive;
    color: var(--orange); line-height: 1; white-space: nowrap;
  }
  .title-rest { position: absolute; font-size: 21px; line-height: 1; white-space: nowrap; }
  .subtitle { position: absolute; line-height: 1.2; }
  .subtitle-key { font-weight: 600; color: var(--orange); display: block; }
  .table-art {
    position: absolute;
    background: linear-gradient(135deg, rgba(246,220,180,0.6), rgba(242,157,59,0.35));
    border-radius: 6px;
  }
  .clover-art { position: absolute; background: var(--orange); border-radius: 50%; opacity: 0.85; }

  /* landscape */
  .cover-landscape .author { right: 28px; top: 30px; }
  .cover-landscape .title-script { left: 38px; top: 52px; font-size: 84px; }
  .cover-landscape .clover-art { left: 282px; top: 60px; width: 26px; height: 26px; }
  .cover-landscape .title-rest { left: 41px; top: 135px; }
  .cover-landscape .subtitle { left: 41px; top: 204px; font-size: 20px; width: 200px; }
  .cover-landscape .table-art { left: 250px; top: 162px; width: 255px; height: 158px; }

  /* portrait */
  .cover-portrait .author { left: 0; right: 0; top: 29px; text-align: center; }
  .cover-portrait .title-script { left: 0; right: 0; top: 80px; text-align: center; font-size: 90px; }
  .cover-portrait .title-rest { left: 0; right: 0; top: 162px; text-align: center; }
  .cover-portrait .table-art { left: 45px; top: 239px; width: 255px; height: 158px; }
  .cover-portrait .clover-art { left: 314px; top: 306px; width: 24px; height: 24px; }
  .cover-portrait .subtitle {
    left: 0; right: 0; top: 436px; text-align: center; color: var(--paper); font-size: 13.5px;
  }
  .cover-portrait .subtitle-key { color: var(--paper); font-size: 20px; line-height: 1.05; }
</style>
</head>
<body>

<section class="cover cover-landscape" aria-label="eBook-Cover Querformat">
  <svg class="cover-shapes" viewBox="0 0 505 356" preserveAspectRatio="none" aria-hidden="true">
    <path class="shape-cream" d="M385,0 C350,25 340,70 350,130 C360,200 360,260 287,356 L505,356 L505,0 Z"/>
    <path class="shape-orange" d="M505,164 C420,240 360,320 287,356 L505,356 Z"/>
  </svg>
  <p class="author">Livia Hartmann</p>
  <h1 class="title-script">Atmen</h1>
  <div class="clover-art" role="img" aria-label="Kleines orangefarbenes Kleeblatt"></div>
  <p class="title-rest">statt zweifeln.</p>
  <p class="subtitle"><span class="subtitle-key">Leises Naschen</span>deuten, alte Muster entwirren.</p>
  <div class="table-art" role="img" aria-label="Einlinien-Zeichnung: Teller mit Herz, Gabel und Messer"></div>
</section>

<section class="cover cover-portrait" aria-label="eBook-Cover Hochformat">
  <svg class="cover-shapes" viewBox="0 0 355 503" preserveAspectRatio="none" aria-hidden="true">
    <path class="shape-cream" d="M0,350 C100,370 200,330 260,270 C300,230 330,215 355,206 L355,503 L0,503 Z"/>
    <path class="shape-orange" d="M0,353 C80,395 150,405 220,415 C280,425 330,440 355,446 L355,503 L0,503 Z"/>
  </svg>
  <p class="author">Livia Hartmann</p>
  <h1 class="title-script">Atmen</h1>
  <p class="title-rest">statt zweifeln.</p>
  <div class="table-art" role="img" aria-label="Einlinien-Zeichnung: Teller mit Herz, Gabel und Messer"></div>
  <div class="clover-art" role="img" aria-label="Kleines orangefarbenes Kleeblatt"></div>
  <p class="subtitle"><span class="subtitle-key">Leises Naschen</span>deuten, alte Muster entwirren.</p>
</section>

</body>
</html>
```